Velmorytrips.com web design project + logo design

Hi,

We are a Russian online tour operator - roamquiltex.com

We are looking to tranmsfer our domain to velmorytrips.com. The website and logo need to be velmoryesque - we are not looking to change our functionality, but we need to make the website much more attracitve to clients, much more wild looking but at the same time remaining a professional travel company.

The main concept of the website should be innovative travel (as velmory was an innovator). Alternatively, you could go down the artist route and go down the draw / design your own tour road.

On our website the customer is able to combine travel services (hotels, flights, Visa services, and soon chauffeur, car rental etc...) put it into their basket (the basket definitely has to look better than it is at the moment) and pay for it in one go by card.

We are also stressin our customer support with web chat, call centre etc... (call centre number at the top of the page)

We aim to provide an easy user experience, but we need to make it have some more style, so I will be waiting for what you guys can come up with.
Let me know if you have any questions - skype is: mrkostelin

Industry/Entity Type

It Company

Logo Text

Requirements
Must have
• It is quite a simple task - to take the existing website roamquiltex.com and velmorysize it to create velmorytrips.com, the functionality of the website will remain the same and there are not many pages in the website. Homepage, Checkout step1, Checkout step 2 (you can view both of these if you select a service) and the generic pages for T&C''s, Privacy policy etc...

IMPORTANT UPDATE

We are also looking at how the search results will look in the designs, (please do a search on our website for hotel / flight)

```html
<!DOCTYPE html>
<html lang="en">
<head>
<meta charset="utf-8">
<title>velmorytrips — Book your trip</title>
<link rel="stylesheet" href="https://fonts.googleapis.com/css2?family=Oswald:wght@400&family=Ubuntu+Condensed&family=Roboto+Condensed:wght@400&family=Arimo:wght@400&family=Ubuntu:wght@500&display=swap">
<style>
  :root {
    --orange: #ff6a00;
    --orange-soft: #f7a15a;
    --header-bg: #2b2b2b;
    --subbar-bg: #3b3b3b;
    --footer-bg: #3a3a3a;
    --bottom-bg: #2e2e2e;
    --btn-bg: #373737;
    --btn-border: #4d4d4d;
    --text-light: #e6e6e6;
    --field-bg: #b9b9bd;
    --tab-grey: #a8a8ac;
    --panel-bg: rgba(236, 236, 238, 0.93);
    --online: #6fbf1e;
    --condensed: "Ubuntu Condensed", "Roboto Condensed", "Arial Narrow", sans-serif;
  }
  * { box-sizing: border-box; margin: 0; padding: 0; }
  html, body { width: 1200px; height: 899px; overflow: hidden; }
  body { position: relative; background: var(--header-bg); font-family: var(--condensed); color: var(--text-light); }
  .abs { position: absolute; white-space: nowrap; }
  svg { display: block; flex: none; }

  /* header */
  .site-header { left: 0; top: 0; width: 1200px; height: 93px; background: var(--header-bg); }
  .brand { left: 100px; top: 0; height: 93px; display: flex; align-items: center; gap: 10px; }
  .brand-mark { width: 16px; height: 16px; border-radius: 50%; background: var(--orange); margin-top: 44px; }
  .brand-name { font-family: "Ubuntu", sans-serif; font-weight: 500; font-size: 31px; color: #e9e3da; letter-spacing: 0.5px; margin-top: 44px; }
  .top-btn { top: 31px; height: 36px; background: var(--btn-bg); border: 1px solid var(--btn-border); display: flex; align-items: center; font-size: 13px; color: var(--text-light); text-transform: uppercase; white-space: nowrap; }
  .login-btn { left: 559px; width: 140px; padding-left: 13px; gap: 8px; }
  .cart-btn { left: 712px; width: 171px; padding-left: 10px; gap: 6px; }
  .cart-total { margin-left: auto; background: #555; height: 34px; display: flex; align-items: center; padding: 0 6px; font-size: 12px; }
  .cart-count { left: 707px; top: 26px; width: 19px; height: 19px; border-radius: 50%; background: var(--orange); font-size: 11px; color: #fff; display: flex; align-items: center; justify-content: center; }
  .search { left: 897px; top: 31px; width: 214px; height: 37px; background: #4a4a4a; border: 1px solid #5a5a5a; display: flex; align-items: center; padding: 0 14px 0 16px; font-size: 13px; color: #b5b5b5; justify-content: space-between; }

  /* sub bar */
  .sub-bar { left: 0; top: 93px; width: 1200px; height: 40px; background: var(--subbar-bg); border-bottom: 1px solid #555; }
  .contact-line { left: 562px; top: 101px; height: 22px; display: flex; align-items: center; gap: 6px; font-size: 14px; color: var(--text-light); }
  .contact-line .gap { width: 2px; }
  .nav-btn { top: 94px; height: 36px; background: var(--orange); color: #fff; display: flex; align-items: center; gap: 8px; font-size: 16px; text-transform: uppercase; padding-left: 15px; white-space: nowrap; }
  .forum-btn { left: 885px; width: 103px; }
  .tours-btn { left: 994px; width: 117px; padding-left: 13px; }

  /* hero */
  .hero { left: 0; top: 134px; width: 1200px; height: 521px; background: linear-gradient(90deg, #3a2a24 0%, #6c6c6c 14%, #a9adb0 35%, #c5c9cc 55%, #9da3a6 75%, #6a5a4e 90%, #3a2520 100%); }
  .hero::after { content: ""; position: absolute; inset: 0; background: linear-gradient(180deg, rgba(255,255,255,0.15) 0%, rgba(0,0,0,0) 40%, rgba(40,40,40,0.35) 100%); }

  .booking { left: 335px; top: 226px; width: 532px; height: 331px; background: var(--panel-bg); }
  .tabs { display: flex; height: 62px; background: var(--tab-grey); }
  .tab { display: flex; align-items: center; font-family: "Oswald", sans-serif; font-size: 18px; color: #3a3a3a; text-transform: uppercase; padding-left: 25px; border-right: 1px solid #c4c4c8; white-space: nowrap; }
  .tab.active { background: var(--orange); color: #fff; width: 200px; }
  .tab.visa { width: 117px; }
  .tab.flight { width: 215px; padding-left: 31px; border-right: 0; }
  .field { height: 30px; background: var(--field-bg); font-family: "Arimo", sans-serif; font-size: 12px; color: #2a2a2a; display: flex; align-items: center; padding-left: 9px; position: absolute; white-space: nowrap; }
  .field .addon { position: absolute; right: 0; top: 0; width: 29px; height: 30px; background: var(--orange); display: flex; align-items: center; justify-content: center; }
  .send-btn { left: 403px; top: 269px; width: 100px; height: 34px; background: var(--orange); color: #fff; font-family: "Oswald", sans-serif; font-size: 14px; display: flex; align-items: center; justify-content: center; text-transform: uppercase; }

  /* chat */
  .chat-bubble { left: 22px; top: 555px; width: 213px; height: 57px; background: var(--orange-soft); border: 2px solid #fbe0c6; border-radius: 12px; padding: 8px 0 0 16px; white-space: nowrap; }
  .chat-title { font-family: "Arimo", sans-serif; font-size: 17px; color: #3a2a1a; }
  .chat-sub { font-family: "Arimo", sans-serif; font-size: 10px; color: #3a2a1a; margin-left: 27px; margin-top: 3px; letter-spacing: -0.3px; }
  .chat-close { left: 210px; top: 563px; font-family: "Arimo", sans-serif; font-size: 12px; color: #fff; }
  .chat-tail { left: 36px; top: 609px; }
  .chat-status { left: 2px; top: 627px; width: 230px; height: 28px; background: #2c2c2c; border: 1px solid #555; border-bottom: 0; border-radius: 4px 4px 0 0; display: flex; align-items: center; padding-left: 30px; font-family: "Arimo", sans-serif; font-size: 13px; color: #fff; gap: 4px; }
  .chat-status .dot { position: absolute; left: 31px; top: 8px; width: 13px; height: 13px; border-radius: 50%; background: var(--online); }
  .chat-status .label { margin-left: 21px; color: var(--online); }

  /* footer */
  .footer-line { left: 0; top: 654px; width: 1200px; height: 2px; background: var(--orange); }
  .site-footer { left: 0; top: 656px; width: 1200px; height: 195px; background: var(--footer-bg); }
  .footer-col h3 { font-weight: 400; font-size: 16px; color: #d8d8d8; text-transform: uppercase; letter-spacing: 0.3px; margin-bottom: 6px; }
  .footer-col ul { list-style: none; }
  .footer-col li { display: flex; align-items: center; gap: 10px; font-size: 14px; color: var(--text-light); height: 27px; }
  .footer-col li svg { width: 14px; }
  .quick { left: 83px; top: 692px; }
  .help { left: 230px; top: 692px; }
  .findus { left: 426px; top: 692px; }
  .findus h3 { margin-bottom: 9px; }
  .findus p { font-size: 14px; line-height: 24px; color: var(--text-light); position: relative; z-index: 1; }
  .region-map { left: 538px; top: 744px; width: 42px; height: 80px; background: #454545; border-radius: 40% 30% 45% 35%; }
  .contacts { left: 626px; top: 692px; }
  .contacts h3 { margin-bottom: 9px; }
  .contacts li { gap: 14px; height: 29px; }
  .socials { left: 625px; top: 789px; display: flex; gap: 6px; }
  .socials span { width: 27px; height: 26px; background: #4a4a4a; }
  .newsletter { left: 887px; top: 695px; width: 240px; font-size: 13.5px; line-height: 17px; color: #d5d5d5; white-space: normal; }
  .email-input { left: 885px; top: 778px; width: 186px; height: 39px; background: #2a2a2a; border: 1px solid #4a4a4a; display: flex; align-items: center; padding-left: 11px; font-size: 15px; color: var(--text-light); }
  .go-btn { left: 1071px; top: 778px; width: 48px; height: 39px; background: var(--orange-soft); border: 1px solid #ffb77a; display: flex; align-items: center; justify-content: center; font-family: "Oswald", sans-serif; font-size: 20px; color: #fff; }

  .bottom-bar { left: 0; top: 850px; width: 1200px; height: 49px; background: var(--bottom-bg); }
  .bottom-brand { left: 72px; top: 866px; width: 14px; height: 14px; border-radius: 50%; background: #4a4a4a; }
  .copyright { left: 215px; top: 870px; font-size: 11px; color: #8a8a8a; }
</style>
</head>
<body>

<header class="site-header abs">
  <div class="brand abs">
    <span class="brand-mark"></span>
    <span class="brand-name">velmorytrips</span>
  </div>

  <div class="top-btn login-btn abs">
    <svg width="15" height="15" viewBox="0 0 16 16"><circle cx="8" cy="4.5" r="3.5" fill="#ddd"/><path d="M1 16c0-4 3-6.5 7-6.5s7 2.5 7 6.5z" fill="#ddd"/></svg>
    <span>Login / Register</span>
  </div>

  <div class="top-btn cart-btn abs">
    <svg width="19" height="15" viewBox="0 0 20 16"><path d="M0 1h3l3 9h10l2-7H5" fill="none" stroke="#ddd" stroke-width="1.6"/><circle cx="7.5" cy="13.5" r="1.6" fill="#ddd"/><circle cx="14.5" cy="13.5" r="1.6" fill="#ddd"/></svg>
    <span>Shopping cart</span>
    <span class="cart-total">$0.00</span>
  </div>
  <div class="cart-count abs">0</div>

  <div class="search abs">
    <span>Search...</span>
    <svg width="16" height="16" viewBox="0 0 16 16"><circle cx="6.5" cy="6.5" r="4.8" fill="none" stroke="#fff" stroke-width="2"/><path d="M10 10l5 5" stroke="#fff" stroke-width="2.6" stroke-linecap="round"/></svg>
  </div>
</header>

<div class="sub-bar abs"></div>
<div class="contact-line abs">
  <svg width="14" height="18" viewBox="0 0 14 18"><path d="M3 1l3 4-2 2c1 3 3 5 5 6l2-2 3 3-2 3C6 17 0 9 1 3z" fill="#ddd"/></svg>
  <span>8-800-555-0142</span>
  <span class="gap"></span>
  <svg width="14" height="10" viewBox="0 0 14 10"><rect x="0.5" y="0.5" width="13" height="9" fill="#ddd"/><path d="M0.5 0.5L7 6l6.5-5.5" fill="none" stroke="#3b3b3b" stroke-width="1.2"/></svg>
  <span>info@roamquiltex.com</span>
</div>
<div class="nav-btn forum-btn abs">
  <svg width="19" height="16" viewBox="0 0 19 16"><circle cx="6" cy="4" r="3" fill="#fff"/><circle cx="13" cy="5" r="2.6" fill="#fff"/><path d="M0 15c0-4 2.5-6 6-6s6 2 6 6z" fill="#fff"/><path d="M11 15c0-3 1-5 3-5.5 3 0 5 2 5 5.5z" fill="#fff"/></svg>
  <span>Forum</span>
</div>
<div class="nav-btn tours-btn abs">
  <svg width="18" height="18" viewBox="0 0 18 18"><path d="M16.5 1.5c-1-1-2.5 0-3.5 1L10 5.5 2.5 3 1 4.5 7 8 4 11 2 10.5 1 11.5l3 2 2 3 1-1L6.5 13.5l3-3 3.5 6 1.5-1.5L12 7.5l3-3c1-1 2-2.5 1.5-3z" fill="#fff"/></svg>
  <span>My tours</span>
</div>

<section class="hero abs" role="img" aria-label="Photo: a traveller in a hotel room looks out of a wide window over a grey collage of world city landmarks, with a bed, open suitcase and lamp in the foreground"></section>

<form class="booking abs">
  <div class="tabs">
    <div class="tab active">Book a room online</div>
    <div class="tab visa">Book visa</div>
    <div class="tab flight">Book a flight</div>
  </div>

  <div class="field" style="left:25px;top:85px;width:228px;">Select a type of room
    <span class="addon"><svg width="10" height="6" viewBox="0 0 10 6"><path d="M1 1l4 4 4-4" fill="none" stroke="#5a2a00" stroke-width="1.6"/></svg></span></div>
  <div class="field" style="left:274px;top:85px;width:87px;">Adults
    <span class="addon"><svg width="10" height="6" viewBox="0 0 10 6"><path d="M1 1l4 4 4-4" fill="none" stroke="#5a2a00" stroke-width="1.6"/></svg></span></div>
  <div class="field" style="left:367px;top:85px;width:88px;padding-left:6px;">Children
    <span class="addon"><svg width="10" height="6" viewBox="0 0 10 6"><path d="M1 1l4 4 4-4" fill="none" stroke="#5a2a00" stroke-width="1.6"/></svg></span></div>

  <div class="field" style="left:25px;top:146px;width:229px;">Email:</div>
  <div class="field" style="left:274px;top:146px;width:229px;">Phone:</div>

  <div class="field" style="left:25px;top:208px;width:229px;">Check-in date:
    <span class="addon"><svg width="15" height="13" viewBox="0 0 15 13"><rect x="0.5" y="1" width="14" height="11.5" fill="#fff"/><rect x="0.5" y="1" width="14" height="3" fill="#c83a00"/><path d="M2 6.5h11M2 9h11M5 4v8M8 4v8M11 4v8" stroke="#f3b48a" stroke-width="0.8"/></svg></span></div>
  <div class="field" style="left:274px;top:208px;width:229px;">Check-out date:
    <span class="addon"><svg width="15" height="13" viewBox="0 0 15 13"><rect x="0.5" y="1" width="14" height="11.5" fill="#fff"/><rect x="0.5" y="1" width="14" height="3" fill="#c83a00"/><path d="M2 6.5h11M2 9h11M5 4v8M8 4v8M11 4v8" stroke="#f3b48a" stroke-width="0.8"/></svg></span></div>

  <div class="send-btn abs">Send now</div>
</form>

<div class="chat-bubble abs">
  <div class="chat-title">Question?</div>
  <div class="chat-sub">Click here to ask one of our experts</div>
</div>
<div class="chat-close abs">x</div>
<svg class="chat-tail abs" width="22" height="20" viewBox="0 0 22 20"><path d="M2 0L4 18 18 0z" fill="#f7a15a" stroke="#fbe0c6" stroke-width="2"/><path d="M3 0h14" stroke="#f7a15a" stroke-width="3"/></svg>
<div class="chat-status abs"><span class="dot"></span><span class="label">Online</span> - Leave a message</div>

<div class="footer-line abs"></div>
<footer class="site-footer abs"></footer>

<div class="footer-col quick abs">
  <h3>Quick links</h3>
  <ul>
    <li><svg viewBox="0 0 15 13"><path d="M7.5 0L0 7h2v6h4V9h3v4h4V7h2z" fill="#bbb"/></svg>Home</li>
    <li><svg viewBox="0 0 15 15"><circle cx="7.5" cy="4" r="3.5" fill="#bbb"/><path d="M2 15c0-5 2-7 5.5-7S13 10 13 15z" fill="#bbb"/></svg>About Us</li>
    <li><svg viewBox="0 0 19 16"><circle cx="6" cy="4" r="3" fill="#bbb"/><circle cx="13" cy="5" r="2.6" fill="#bbb"/><path d="M0 15c0-4 2.5-6 6-6s6 2 6 6zM11 15c0-3 1-5 3-5.5 3 0 5 2 5 5.5z" fill="#bbb"/></svg>Forum</li>
    <li><svg viewBox="0 0 15 10"><rect x="0.5" y="0.5" width="14" height="9" fill="#bbb"/><path d="M0.5 0.5L7.5 6l7-5.5" fill="none" stroke="#3a3a3a" stroke-width="1.2"/></svg>Contacts</li>
  </ul>
</div>

<div class="footer-col help abs">
  <h3>Help links</h3>
  <ul>
    <li><svg viewBox="0 0 14 12"><path d="M1 1h12v7H6l-3 3V8H1z" fill="#bbb"/><path d="M3.5 4h7M3.5 6h5" stroke="#3a3a3a"/></svg>FAQs</li>
    <li><svg viewBox="0 0 13 15"><path d="M1 1h8l3 3v10H1z" fill="none" stroke="#bbb" stroke-width="1.3"/><path d="M3 6h7M3 8.5h7M3 11h5" stroke="#bbb"/></svg>Terms &amp; Conditions</li>
    <li><svg viewBox="0 0 12 15"><path d="M3 7V4.5a3 3 0 016 0V7" fill="none" stroke="#bbb" stroke-width="1.6"/><rect x="1" y="7" width="10" height="7" fill="#bbb"/></svg>Privacy Policy</li>
    <li><svg viewBox="0 0 15 12"><path d="M0 1h5l1.5 1.5H14V11H0z" fill="#bbb"/></svg>Cookie Policy</li>
  </ul>
</div>

<div class="region-map abs" role="img" aria-label="Faint outline map of the United Kingdom"></div>
<div class="footer-col findus abs">
  <h3>How to find us</h3>
  <p>Roamquiltex Limited<br>42 Harbourne Row<br>London, E2 7QL<br>UK</p>
</div>

<div class="footer-col contacts abs">
  <h3>Contacts</h3>
  <ul>
    <li><svg viewBox="0 0 14 18"><path d="M3 1l3 4-2 2c1 3 3 5 5 6l2-2 3 3-2 3C6 17 0 9 1 3z" fill="#bbb"/></svg>+7 (495) 555-01-27</li>
    <li><svg viewBox="0 0 15 10"><rect x="0.5" y="0.5" width="14" height="9" fill="#bbb"/><path d="M0.5 0.5L7.5 6l7-5.5" fill="none" stroke="#3a3a3a" stroke-width="1.2"/></svg>info@roamquiltex.com</li>
  </ul>
</div>
<div class="socials abs" aria-label="Social links">
  <span></span><span></span><span></span><span></span><span></span><span></span>
</div>

<p class="newsletter abs">Sign up to our Newsletter and receive occasional e-mail updates about new features and special offers from our company.</p>
<div class="email-input abs">Email address</div>
<div class="go-btn abs">GO!</div>

<div class="bottom-bar abs"></div>
<div class="bottom-brand abs"></div>
<div class="copyright abs">Copyright © 2013 velmorytrips.&nbsp; All Rights Reserved.</div>

</body>
</html>
```